Very Simple/Minimal Business Card Design Project

The company operates in the industrial maritime infrastructure sector in Brazil. You can find more information on our website www.navelquor.com.br WE NEED TO LOOK POWERFUL AND SERIOUS
I have attached a copy of the old cards. We would like something more professional / industrial / sexy that also includes the position.

The card can be double sided or not. We would like you to propose as many options.

Thank you
Updates

Many thanks, do let me know if you have any questions. I am under a lot of time pressure to try and have them printed over the next days or so.

Please could you use the following information

for the address: Rua Tapiraçu, 418 - Centro, Rio de Janeiro, 20135-070, Brasil

for the mobile: +55 21 8372 9041
for the landline: +55 21 4067 3859

and position:  Diretor Geral

Thakn you

Target Market(s)

Shipowners, bankers, industrial companies

Industry/Entity Type

Industrial

Requirements
Must have
• POWERFUL
SERIOUS
SOLID
BIG CORPORATION

```html
<!DOCTYPE html>
<html lang="pt-BR">
<head>
<meta charset="UTF-8">
<title>Navelquor — Cartão de Visita</title>
<link rel="stylesheet" href="https://fonts.googleapis.com/css2?family=Source+Sans+3:ital,wght@0,400;0,600;0,700;0,900;1,400&display=swap">
<style>
  :root {
    --navy: #0b1a98;
    --navy-deep: #071270;
    --green: #23dc00;
    --white: #ffffff;
    --text-light: #ffffff;
  }
  html, body {
    margin: 0;
    padding: 0;
    width: 1200px;
    height: 768px;
    overflow: hidden;
    background: var(--white);
  }
  .card {
    position: relative;
    width: 1200px;
    height: 768px;
    background: var(--white);
    font-family: "Source Sans 3", "Myriad Pro", sans-serif;
    overflow: hidden;
  }
  .brand {
    position: absolute;
    left: 0;
    top: 57px;
    width: 1200px;
    height: 158px;
    display: flex;
    justify-content: center;
    align-items: center;
    gap: 28px;
  }
  .brand-square {
    width: 150px;
    height: 150px;
    background: var(--green);
    flex: none;
  }
  .brand-name {
    font-weight: 900;
    font-size: 112px;
    line-height: 1;
    color: var(--navy);
    letter-spacing: 4px;
  }
  .navy-band {
    position: absolute;
    left: 0;
    top: 256px;
    width: 1200px;
    height: 49px;
    background: var(--navy);
  }
  .contact-panel {
    position: absolute;
    left: 0;
    top: 346px;
    width: 1200px;
    height: 422px;
    background: var(--green);
    color: var(--text-light);
  }
  .person-name {
    position: absolute;
    left: 0;
    width: 1200px;
    top: 26px;
    margin: 0;
    text-align: center;
    font-weight: 700;
    font-size: 50px;
    line-height: 1;
  }
  .position {
    position: absolute;
    left: 0;
    width: 1200px;
    top: 86px;
    margin: 0;
    text-align: center;
    font-weight: 700;
    font-size: 26px;
    line-height: 1;
    letter-spacing: 6px;
    text-transform: uppercase;
    color: var(--navy-deep);
  }
  .website {
    position: absolute;
    left: 0;
    width: 1200px;
    top: 124px;
    margin: 0;
    text-align: center;
    font-style: italic;
    font-size: 32px;
    line-height: 1;
  }
  .details {
    position: absolute;
    top: 200px;
    margin: 0;
    font-size: 34px;
    line-height: 47.5px;
    font-style: normal;
  }
  .address { left: 128px; }
  .phones { left: 608px; }
  .details span { display: block; }
</style>
</head>
<body>
  <div class="card">
    <div class="brand">
      <div class="brand-square"></div>
      <div class="brand-name">NAVELQUOR</div>
    </div>

    <div class="navy-band"></div>

    <section class="contact-panel">
      <h1 class="person-name">Henrique Valmont</h1>
      <p class="position">Diretor Geral</p>
      <p class="website">www.navelquor.com.br</p>

      <address class="details address">
        <span>Rua Tapiraçu, 418</span>
        <span>Centro</span>
        <span>CEP 20135-070</span>
        <span>Rio de Janeiro</span>
      </address>

      <p class="details phones">
        <span>T: + 55 21 4067 3859</span>
        <span>M: + 55 21 8372 9041</span>
        <span>henrique@navelquor.com.br</span>
      </p>
    </section>
  </div>
</body>
</html>
```